Hip / Cool Business Card for Custom Accessory Company

I would like to get a 2 sided design for standard size business cards, glossy (2 inches x 3.5 inches). Can be landscape or portrait layout! The design should include our logo (attached). The card should be extremely clear that the company is Tin Lantern. Should also have our URL clear. Should also use the color scheme seen on our upcoming site, tinlantern.example. The font we use is called "hurry up." Other than that, please go-to-town. We are targeting 15-45 y.o. market, with a skew on the 20-30 crowd. We do custom and stock iPhone cases as well as Cufflinks, Winestoppers; see the website for more.
Updates

Project Deadline Extended
Reason: Extending in case the US July 4th Holiday is keeping people from working!!

Industry/Entity Type

Landscape

Requirements
Must have
• Must be clear that the website is tinlantern.example. Must be clear that custom designs are an option.
Nice to have
• images of our designs. examples of our designs.
Should not have
• hard on the eyes contrasting colors such as orange on black. green on blue. Should not have any fonts that are considered "old" like Times New Roman. But decorative fonts are fine.

```html
<!DOCTYPE html>
<html lang="en">
<head>
<meta charset="utf-8">
<title>Tin Lantern – Business Card Designs</title>
<link href="https://fonts.googleapis.com/css2?family=Audiowide&family=Orbitron:wght@500&display=swap" rel="stylesheet">
<style>
  :root {
    --backdrop: #3b302c;
    --card: #ffffff;
    --teal: #1b9fae;
    --sky: #5cc8ef;
    --pale: #cfe9ee;
    --ink: #151515;
    --label: #f4f1ee;
  }
  * { box-sizing: border-box; margin: 0; padding: 0; }
  html, body { width: 1200px; height: 900px; overflow: hidden; }
  body {
    position: relative;
    background: var(--backdrop);
    font-family: "Audiowide", sans-serif;
    color: var(--ink);
  }
  .design-label {
    position: absolute;
    font-family: "Audiowide", sans-serif;
    font-size: 26px;
    letter-spacing: 5px;
    color: var(--label);
  }
  .design-label--one { left: 65px; top: 220px; }
  .design-label--two { left: 770px; top: 815px; }

  .card {
    position: absolute;
    background: var(--card);
    overflow: hidden;
    box-shadow: 0 4px 14px rgba(0,0,0,.35);
  }
  .card--portrait { width: 230px; height: 402px; }
  .card--landscape { width: 430px; height: 246px; }

  .band { position: absolute; left: 0; width: 100%; display: block; }
  .band--top { top: 0; height: 14px; }
  .band--bottom { bottom: 10px; height: 14px; }
  .band--back-top { top: 0; height: 18px; }
  .band--back-bottom { bottom: 0; height: 24px; }
  .band--side { position: absolute; top: 0; height: 100%; width: 20px; display: block; }
  .band--left { left: 0; }
  .band--right { right: 0; }

  .name-tag {
    position: absolute; top: 22px; left: 48px;
    width: 118px; height: 18px;
    background: var(--sky);
    color: #fff; font-size: 9px; letter-spacing: 1px;
    padding: 4px 0 0 12px;
  }
  .role {
    position: absolute; top: 44px; right: 64px;
    font-size: 7px; font-family: "Orbitron", sans-serif;
  }

  .wordmark {
    position: absolute; left: 0; width: 100%;
    display: flex; align-items: center; justify-content: center; gap: 10px;
  }
  .wordmark__dot { border-radius: 50%; background: var(--teal); flex: none; }
  .wordmark__name {
    font-family: "Audiowide", sans-serif;
    color: var(--ink); line-height: 1.05; text-transform: uppercase;
  }
  .card--front .wordmark { top: 120px; }
  .card--front .wordmark__dot { width: 34px; height: 34px; }
  .card--front .wordmark__name { font-size: 26px; }

  .contact-list { position: absolute; top: 246px; left: 20px; right: 0; list-style: none; }
  .contact-item {
    height: 26px; margin-bottom: 9px;
    background: var(--sky);
    display: flex; align-items: center; gap: 10px;
    padding-left: 12px;
    font-size: 8px; color: var(--ink);
  }
  .contact-item svg { width: 13px; height: 13px; flex: none; }

  .card--back .wordmark { top: 130px; }
  .card--back .wordmark__dot { width: 40px; height: 40px; }
  .card--back .wordmark__name { font-size: 30px; }
  .site-url {
    position: absolute; left: 0; width: 100%; text-align: center;
    color: var(--teal); font-family: "Audiowide", sans-serif;
    letter-spacing: 3px;
  }
  .card--back .site-url { bottom: 62px; font-size: 13px; }
  .card--landscape .wordmark { top: 44px; }
  .card--landscape .wordmark__dot { width: 38px; height: 38px; }
  .card--landscape .wordmark__name { font-size: 30px; }
  .card--landscape .site-url { bottom: 44px; font-size: 19px; letter-spacing: 4px; }
</style>
</head>
<body>

<span class="design-label design-label--one">DESIGN 1</span>
<span class="design-label design-label--two">DESIGN 2</span>

<!-- Design 1 : front -->
<section class="card card--portrait card--front" style="left:330px; top:40px;">
  <svg class="band band--top" viewBox="0 0 230 14" preserveAspectRatio="none">
    <rect width="230" height="14" fill="var(--teal)"/>
    <polygon points="95,0 165,0 150,14 80,14" fill="var(--pale)"/>
  </svg>
  <div class="name-tag">YOUR NAME</div>
  <div class="role">CEO</div>
  <div class="wordmark">
    <span class="wordmark__dot"></span>
    <span class="wordmark__name">Tin<br>Lantern</span>
  </div>
  <ul class="contact-list">
    <li class="contact-item">
      <svg viewBox="0 0 14 14"><rect x="3" y="1" width="8" height="12" rx="1.5" fill="none" stroke="#fff" stroke-width="1.3"/></svg>
      +41 26 555 01 23
    </li>
    <li class="contact-item">
      <svg viewBox="0 0 14 14"><rect x="1" y="3" width="12" height="8" fill="none" stroke="#fff" stroke-width="1.2"/><polyline points="1,3 7,8 13,3" fill="none" stroke="#fff" stroke-width="1.2"/></svg>
      INFO@TINLANTERN.EXAMPLE
    </li>
    <li class="contact-item">
      <svg viewBox="0 0 14 14"><path d="M7 13 C3 8 2.5 6.5 2.5 5 A4.5 4.5 0 0 1 11.5 5 C11.5 6.5 11 8 7 13 Z" fill="#fff"/><circle cx="7" cy="5" r="1.6" fill="var(--sky)"/></svg>
      RUE DES LANTERNES 4 FRIBOURG
    </li>
  </ul>
  <svg class="band band--bottom" viewBox="0 0 230 14" preserveAspectRatio="none">
    <rect width="230" height="14" fill="var(--teal)"/>
    <polygon points="130,0 190,0 175,14 115,14" fill="var(--pale)"/>
  </svg>
</section>

<!-- Design 1 : back -->
<section class="card card--portrait card--back" style="left:650px; top:40px; width:280px; height:402px;">
  <svg class="band band--back-top" viewBox="0 0 280 18" preserveAspectRatio="none">
    <rect width="280" height="18" fill="var(--teal)"/>
    <polygon points="150,0 230,0 215,18 135,18" fill="var(--pale)"/>
  </svg>
  <div class="wordmark">
    <span class="wordmark__dot"></span>
    <span class="wordmark__name">Tin<br>Lantern</span>
  </div>
  <div class="site-url">WWW.TINLANTERN.EXAMPLE</div>
  <svg class="band band--back-bottom" viewBox="0 0 280 24" preserveAspectRatio="none">
    <rect width="280" height="24" fill="var(--teal)"/>
    <polygon points="110,0 190,0 175,24 95,24" fill="var(--pale)"/>
  </svg>
</section>

<!-- Design 2 : front -->
<section class="card card--portrait card--front" style="left:330px; top:478px;">
  <svg class="band band--top" viewBox="0 0 230 14" preserveAspectRatio="none">
    <rect width="230" height="14" fill="var(--teal)"/>
    <polygon points="95,0 165,0 150,14 80,14" fill="var(--pale)"/>
  </svg>
  <div class="name-tag">YOUR NAME</div>
  <div class="role">CEO</div>
  <div class="wordmark">
    <span class="wordmark__dot"></span>
    <span class="wordmark__name">Tin<br>Lantern</span>
  </div>
  <ul class="contact-list">
    <li class="contact-item">
      <svg viewBox="0 0 14 14"><rect x="3" y="1" width="8" height="12" rx="1.5" fill="none" stroke="#fff" stroke-width="1.3"/></svg>
      +41 26 555 01 23
    </li>
    <li class="contact-item">
      <svg viewBox="0 0 14 14"><rect x="1" y="3" width="12" height="8" fill="none" stroke="#fff" stroke-width="1.2"/><polyline points="1,3 7,8 13,3" fill="none" stroke="#fff" stroke-width="1.2"/></svg>
      INFO@TINLANTERN.EXAMPLE
    </li>
    <li class="contact-item">
      <svg viewBox="0 0 14 14"><path d="M7 13 C3 8 2.5 6.5 2.5 5 A4.5 4.5 0 0 1 11.5 5 C11.5 6.5 11 8 7 13 Z" fill="#fff"/><circle cx="7" cy="5" r="1.6" fill="var(--sky)"/></svg>
      RUE DES LANTERNES 4 FRIBOURG
    </li>
  </ul>
  <svg class="band band--bottom" viewBox="0 0 230 14" preserveAspectRatio="none">
    <rect width="230" height="14" fill="var(--teal)"/>
    <polygon points="130,0 190,0 175,14 115,14" fill="var(--pale)"/>
  </svg>
</section>

<!-- Design 2 : back (landscape) -->
<section class="card card--landscape" style="left:620px; top:520px;">
  <svg class="band band--side band--left" viewBox="0 0 20 246" preserveAspectRatio="none">
    <rect width="20" height="246" fill="var(--teal)"/>
    <polygon points="0,60 20,45 20,125 0,140" fill="var(--pale)"/>
  </svg>
  <div class="wordmark">
    <span class="wordmark__dot"></span>
    <span class="wordmark__name">Tin<br>Lantern</span>
  </div>
  <div class="site-url">WWW.TINLANTERN.EXAMPLE</div>
  <svg class="band band--side band--right" viewBox="0 0 20 246" preserveAspectRatio="none">
    <rect width="20" height="246" fill="var(--teal)"/>
    <polygon points="0,110 20,95 20,175 0,190" fill="var(--pale)"/>
  </svg>
</section>

</body>
</html>
```